Business Card Design

TAX PREPARATION CO.
INCOME & SALES TAXES
ELECTRONIC FILING
ESTABLISHED IN 1993
Looking for a design with a lady at a table with a pen over a 1040 form looking puzzled and a bubble with wording I'm in over my head.

Industry/Entity Type

Business

Contact Information for Business Card

LEDGERLY PLUS INC

```html
<!DOCTYPE html>
<html lang="en">
<head>
<meta charset="utf-8">
<title>Ledgerly Plus Inc — Business Card</title>
<link rel="stylesheet" href="https://fonts.googleapis.com/css2?family=Josefin+Sans:wght@400;600&family=Nunito+Sans:wght@400&display=swap">
<style>
  :root {
    --stage: #e4e4e2;
    --card: #ffffff;
    --brand-blue: #1e9fdc;
    --brand-red: #e0262c;
    --ink: #2b2b2d;
    --photo-light: #efece8;
    --photo-warm: #cfc8c0;
    --photo-mid: #8d8a88;
    --photo-dark: #3b3c40;
    --photo-deep: #26272b;
    --bubble: #ffffff;
    --bubble-edge: #d6d6d6;
  }
  * { margin: 0; padding: 0; box-sizing: border-box; }
  html, body {
    width: 1200px; height: 692px; overflow: hidden;
    background: var(--stage);
  }
  .business-card {
    position: absolute; left: 110px; top: 66px;
    width: 980px; height: 560px;
    background: var(--card);
    overflow: hidden;
    box-shadow: 0 8px 24px rgba(0,0,0,0.18);
  }
  .hero-photo {
    position: absolute; right: 0; top: 0;
    width: 560px; height: 100%;
    background: linear-gradient(150deg,
      var(--photo-light) 0%,
      var(--photo-warm) 30%,
      var(--photo-mid) 50%,
      var(--photo-dark) 68%,
      var(--photo-deep) 100%);
  }
  .hero-photo__fade {
    position: absolute; inset: 0;
    background:
      linear-gradient(90deg, var(--card) 0%, rgba(255,255,255,0.85) 14%, rgba(255,255,255,0) 38%),
      linear-gradient(180deg, rgba(255,255,255,0) 72%, rgba(255,255,255,0.85) 100%);
  }
  .thought-bubble {
    position: absolute; left: 700px; top: 14px;
    width: 190px; height: 140px;
  }
  .thought-bubble svg { position: absolute; inset: 0; }
  .thought-bubble__text {
    position: absolute; left: 0; top: 24px; width: 190px;
    text-align: center;
    font-family: "Nunito Sans", Arial, sans-serif;
    font-size: 22px; line-height: 1.05;
    color: var(--ink);
  }
  .brand {
    position: absolute; left: 78px; top: 150px;
    font-family: "Josefin Sans", Arial, sans-serif;
  }
  .brand__row { display: flex; align-items: center; gap: 14px; }
  .brand__name {
    font-weight: 600; font-size: 40px; letter-spacing: 1px;
    color: var(--brand-blue);
  }
  .brand__mark {
    width: 14px; height: 14px; border-radius: 50%;
    background: var(--brand-red);
    margin-bottom: 6px;
  }
  .brand__est {
    margin-top: 2px;
    font-weight: 400; font-size: 26px; letter-spacing: 1px;
    color: var(--ink);
  }
  .services {
    position: absolute; left: 78px; top: 392px;
    list-style: none;
    font-family: "Josefin Sans", Arial, sans-serif;
    font-weight: 400; font-size: 31px; line-height: 1.2;
    letter-spacing: 1px;
    color: var(--ink);
  }
</style>
</head>
<body>
  <div class="business-card">
    <div class="hero-photo" role="img" aria-label="Photo of a woman at a desk holding a pencil over a tax form, looking puzzled">
      <div class="hero-photo__fade"></div>
    </div>

    <div class="thought-bubble">
      <svg width="190" height="140" viewBox="0 0 190 140" aria-hidden="true">
        <ellipse cx="95" cy="50" rx="88" ry="44" fill="var(--bubble)" stroke="var(--bubble-edge)" stroke-width="1"/>
        <circle cx="62" cy="108" r="9" fill="var(--bubble)" stroke="var(--bubble-edge)" stroke-width="1"/>
        <circle cx="48" cy="128" r="5" fill="var(--bubble)" stroke="var(--bubble-edge)" stroke-width="1"/>
      </svg>
      <p class="thought-bubble__text">I'm in over<br>my head</p>
    </div>

    <div class="brand">
      <div class="brand__row">
        <div class="brand__name">LEDGERLY PLUS INC</div>
        <span class="brand__mark" aria-hidden="true"></span>
      </div>
      <div class="brand__est">ESTD 1993</div>
    </div>

    <ul class="services">
      <li>TAX PREPARATION CO.</li>
      <li>INCOME &amp; SALES TAXES</li>
      <li>ELECTRONIC FILING</li>
    </ul>
  </div>
</body>
</html>
```